Independence Day Graphics for Sale

I want to create 10 social media graphics (new Pictora size 4:5 (1080 x 1350 pixels) focusing on our July 4th Sale Graphics, using any of the pics attached. Use the attached pics, NO RANDOM STOCK PHOTOGRAPHY. For the color scheme of the graphics, they should all be complementary to the product colors in the photos.
You can add any of the photos attached but none are required. You can do some of the graphics in all text. I mainly need BOLD text that says one of the headlines (10 total) SEE ATTACHED WORD DOCUMENT for the headlines to use.

Target Market(s)

women looking to lose weight

Requirements
Must have
• pics attached and text attached

```html
<!DOCTYPE html>
<html lang="en">
<head>
<meta charset="utf-8">
<title>Independence Day Sale Graphics</title>
<link rel="stylesheet" href="https://fonts.googleapis.com/css2?family=Bebas+Neue&display=swap">
<style>
  :root {
    --ink: #ffffff;
    --page: #ffffff;
    --red: #d8243f;
    --rose: #e0457f;
    --magenta: #b8378a;
    --plum: #7a3a82;
    --violet: #9a5aa8;
    --indigo: #3a46a6;
    --sky: #5d86c8;
    --mint: #8cc4a6;
    --teal: #2f6a66;
    --counter: #efedea;
    --counter-edge: #e2dfdb;
    --model-top: #f4f1f0;
    --model-mid: #b98a72;
    --model-low: #2a2426;
  }
  * { box-sizing: border-box; margin: 0; padding: 0; }
  html, body { width: 1200px; height: 600px; overflow: hidden; background: var(--page); }
  .board { position: relative; width: 1200px; height: 600px; }

  .tile {
    position: absolute; width: 220px; height: 275px; overflow: hidden;
    font-family: "Bebas Neue", "Oswald", sans-serif; color: var(--ink);
  }
  .row-top { top: 20px; }
  .row-bottom { top: 305px; }
  .col-1 { left: 28px; } .col-2 { left: 259px; } .col-3 { left: 490px; }
  .col-4 { left: 720px; } .col-5 { left: 951px; }

  .tile--red    { background: linear-gradient(160deg, var(--rose) 0%, var(--magenta) 35%, var(--red) 80%); }
  .tile--blue   { background: linear-gradient(200deg, var(--sky) 0%, var(--violet) 40%, var(--indigo) 100%); }
  .tile--plum   { background: linear-gradient(150deg, var(--violet) 0%, var(--magenta) 45%, var(--plum) 100%); }
  .tile--berry  { background: linear-gradient(200deg, var(--magenta) 0%, var(--violet) 45%, var(--plum) 100%); }
  .tile--fade   { background: linear-gradient(180deg, #4a3f8f 0%, #8a4f9e 30%, #c9a4cf 55%, #f2eef2 75%); }
  .tile--fade-rose { background: linear-gradient(180deg, #6a3a7a 0%, #b8478a 32%, #e6c3d8 58%, #f4f1f2 78%); }
  .tile--sea    { background: linear-gradient(170deg, var(--mint) 0%, var(--teal) 40%, #3d4a96 75%, var(--indigo) 100%); }
  .tile--crimson{ background: linear-gradient(200deg, var(--magenta) 0%, #c8305c 50%, var(--red) 100%); }
  .tile--dusk   { background: linear-gradient(180deg, #3f4aa0 0%, #7a4e9e 50%, var(--magenta) 100%); }
  .tile--green  { background: linear-gradient(180deg, #6a9a8a 0%, var(--teal) 60%, #2d5f63 100%); }

  .headline { position: absolute; inset: 0; z-index: 2; }
  .line {
    position: absolute; top: var(--t); font-size: var(--fs);
    line-height: 0.72; white-space: nowrap; letter-spacing: 0.2px;
  }
  .headline--left .line { left: var(--x); }
  .headline--center .line { left: 0; right: 0; text-align: center; }
  .th { font-size: 0.5em; vertical-align: top; line-height: 1; }

  .photo-model {
    position: absolute; z-index: 1; border-radius: 48px 48px 0 0;
    background: linear-gradient(180deg, var(--model-low) 0%, var(--model-mid) 22%, var(--model-top) 40%, var(--model-top) 62%, var(--model-mid) 74%, var(--model-low) 86%);
    opacity: 0.9;
  }
  .photo-counter {
    position: absolute; left: 0; right: 0; bottom: 0; z-index: 1;
    background: linear-gradient(180deg, var(--counter-edge), var(--counter));
  }
  .photo-bottles {
    position: absolute; left: 8px; right: 8px; bottom: 0; z-index: 1;
    background: linear-gradient(180deg, rgba(255,255,255,0.5), #f3f1f0);
    border-radius: 10px 10px 0 0;
  }
</style>
</head>
<body>
<main class="board">

  <!-- Row 1 -->
  <section class="tile tile--red row-top col-1">
    <div class="photo-model" style="left:121px; top:40px; width:99px; height:202px;" role="img" aria-label="Smiling woman in a white cropped sweater holding a supplement bottle"></div>
    <div class="photo-counter" style="height:33px;" role="img" aria-label="Marble counter with supplement bottles"></div>
    <div class="headline headline--left" style="--x:16px">
      <span class="line" style="--t:28px; --fs:39px">July 4<span class="th">th</span></span>
      <span class="line" style="--t:63px; --fs:59px">Mega</span>
      <span class="line" style="--t:113px; --fs:57px">Sale!</span>
      <span class="line" style="--t:160px; --fs:36px">25% Off</span>
      <span class="line" style="--t:191px; --fs:25px">Everything</span>
    </div>
  </section>

  <section class="tile tile--blue row-top col-2">
    <div class="photo-model" style="left:118px; top:30px; width:102px; height:218px;" role="img" aria-label="Smiling woman in a white cropped sweater pointing down at the products"></div>
    <div class="photo-counter" style="height:27px;" role="img" aria-label="Marble counter with three supplement bottles"></div>
    <div class="headline headline--left" style="--x:20px">
      <span class="line" style="--t:36px; --fs:32px">Biggest</span>
      <span class="line" style="--t:66px; --fs:26px">4<span class="th">th</span> of July</span>
      <span class="line" style="--t:90px; --fs:48px">Sale</span>
      <span class="line" style="--t:135px; --fs:44px">Ever!</span>
      <span class="line" style="--t:172px; --fs:34px">25% Off</span>
      <span class="line" style="--t:199px; --fs:31px">Sitewide</span>
    </div>
  </section>

  <section class="tile tile--plum row-top col-3">
    <div class="headline headline--center">
      <span class="line" style="--t:23px; --fs:51px">Historic</span>
      <span class="line" style="--t:68px; --fs:43px">4<span class="th">th</span> of July</span>
      <span class="line" style="--t:108px; --fs:82px">Sale!</span>
      <span class="line" style="--t:180px; --fs:51px">25% Off</span>
      <span class="line" style="--t:225px; --fs:34px">of Everything</span>
    </div>
  </section>

  <section class="tile tile--berry row-top col-4">
    <div class="photo-model" style="left:114px; top:15px; width:106px; height:243px;" role="img" aria-label="Smiling woman in a white cropped sweater pointing down at the products"></div>
    <div class="photo-counter" style="height:17px;" role="img" aria-label="Marble counter with three supplement bottles"></div>
    <div class="headline headline--left" style="--x:20px">
      <span class="line" style="--t:32px; --fs:44px">Mega</span>
      <span class="line" style="--t:70px; --fs:32px">Summer</span>
      <span class="line" style="--t:103px; --fs:26px">Blowout!</span>
      <span class="line" style="--t:125px; --fs:55px">25%</span>
      <span class="line" style="--t:169px; --fs:55px">Off</span>
      <span class="line" style="--t:212px; --fs:23px">Everything</span>
    </div>
  </section>

  <section class="tile tile--fade row-top col-5">
    <div class="photo-bottles" style="height:102px;" role="img" aria-label="Row of four supplement bottles"></div>
    <div class="headline headline--center">
      <span class="line" style="--t:30px; --fs:37px">One-Time Only:</span>
      <span class="line" style="--t:64px; --fs:60px">25% Off</span>
      <span class="line" style="--t:114px; --fs:36px">of Everything!</span>
    </div>
  </section>

  <!-- Row 2 -->
  <section class="tile tile--fade-rose row-bottom col-1">
    <div class="photo-bottles" style="height:108px;" role="img" aria-label="Group of four supplement bottles on a white surface"></div>
    <div class="headline headline--center">
      <span class="line" style="--t:27px; --fs:46px">25% Off</span>
      <span class="line" style="--t:71px; --fs:25px">Stock-Up Event:</span>
      <span class="line" style="--t:96px; --fs:46px">25% Off</span>
      <span class="line" style="--t:134px; --fs:24px">All Supplements</span>
    </div>
  </section>

  <section class="tile tile--sea row-bottom col-2">
    <div class="headline headline--center">
      <span class="line" style="--t:32px; --fs:38px">The Lowest</span>
      <span class="line" style="--t:69px; --fs:64px">Prices</span>
      <span class="line" style="--t:121px; --fs:38px">We've Ever</span>
      <span class="line" style="--t:156px; --fs:50px">Offered!</span>
      <span class="line" style="--t:201px; --fs:54px">25% Off</span>
    </div>
  </section>

  <section class="tile tile--crimson row-bottom col-3">
    <div class="photo-model" style="left:112px; top:25px; width:108px; height:218px;" role="img" aria-label="Smiling woman in a white cropped sweater holding a supplement bottle"></div>
    <div class="photo-counter" style="height:32px;" role="img" aria-label="Marble counter with supplement bottles"></div>
    <div class="headline headline--left" style="--x:10px">
      <span class="line" style="--t:17px; --fs:27px">Our Biggest</span>
      <span class="line" style="--t:40px; --fs:34px">Discount</span>
      <span class="line" style="--t:67px; --fs:50px">Ever!</span>
      <span class="line" style="--t:107px; --fs:64px">25%</span>
      <span class="line" style="--t:157px; --fs:62px">Off</span>
      <span class="line" style="--t:207px; --fs:25px">Everything</span>
    </div>
  </section>

  <section class="tile tile--dusk row-bottom col-4">
    <div class="photo-model" style="left:87px; top:15px; width:133px; height:233px;" role="img" aria-label="Smiling woman in a white cropped sweater pointing down at the products"></div>
    <div class="photo-counter" style="height:27px;" role="img" aria-label="Marble counter with three supplement bottles"></div>
    <div class="headline headline--left" style="--x:13px">
      <span class="line" style="--t:32px; --fs:34px">Don't</span>
      <span class="line" style="--t:64px; --fs:37px">Wait!</span>
      <span class="line" style="--t:97px; --fs:43px">25%</span>
      <span class="line" style="--t:133px; --fs:50px">Off</span>
      <span class="line" style="--t:171px; --fs:37px">Ends</span>
      <span class="line" style="--t:200px; --fs:37px">Soon</span>
    </div>
  </section>

  <section class="tile tile--green row-bottom col-5">
    <div class="photo-model" style="left:86px; top:32px; width:134px; height:218px;" role="img" aria-label="Smiling woman in a white cropped sweater pointing down at the products"></div>
    <div class="photo-counter" style="height:25px;" role="img" aria-label="Counter with a full line of supplement bottles and pouches"></div>
    <div class="headline headline--left" style="--x:20px">
      <span class="line" style="--t:18px; --fs:34px">Last</span>
      <span class="line" style="--t:51px; --fs:21px">Chance</span>
      <span class="line" style="--t:74px; --fs:41px">25%</span>
      <span class="line" style="--t:109px; --fs:46px">Off</span>
      <span class="line" style="--t:147px; --fs:25px">Time Is</span>
      <span class="line" style="--t:172px; --fs:21px">Running</span>
      <span class="line" style="--t:194px; --fs:19px">Out!</span>
    </div>
  </section>

</main>
</body>
</html>
```